KVR Noblesville Sign

I need to have a sign designed for a new self-storage facility we are going to be opening. The sign will be 4'W X 8'H.

Industry/Entity Type

Self Storage

Requirements
Must have
• Harbor Locker Yard logo at the top of the sign, under the logo I want the rendering.
• I also must have this information on the sign:
• 1. OPENING FALL 2016
• 2. Your premier self-storage facility.
• 3. www.harborlockeryard.example

```html
<!DOCTYPE html>
<html lang="en">
<head>
<meta charset="utf-8">
<title>Harbor Locker Yard – Opening Sign</title>
<link rel="stylesheet" href="https://fonts.googleapis.com/css2?family=Oswald:wght@300;400;500;700&display=swap">
<style>
  :root {
    --backdrop: #e6e9ec;
    --sign-white: #ffffff;
    --band-dark: #0d0d0d;
    --band-mid: #3a3a3a;
    --brand-yellow: #f6e61c;
    --accent-green: #2f9a3c;
    --accent-green-light: #6cc04a;
    --gold-dark: #7f6334;
    --gold-light: #c8a96c;
    --ink: #1a1a1a;
  }
  * { margin: 0; padding: 0; box-sizing: border-box; }
  html, body {
    width: 1200px; height: 946px; overflow: hidden;
    background: var(--backdrop);
    font-family: "Oswald", "Arial Narrow", sans-serif;
  }
  .sign {
    position: absolute; left: 410px; top: 33px;
    width: 380px; height: 880px;
    background: var(--sign-white);
    overflow: hidden;
    box-shadow: 0 6px 24px rgba(0,0,0,.18);
  }
  .sign-top {
    position: absolute; inset: 0;
  }
  .brand-name {
    position: absolute; left: 0; right: 0; top: 40px;
    text-align: center;
    color: var(--brand-yellow);
    font-weight: 700;
    font-size: 62px; line-height: 1.05;
    text-transform: none;
  }
  .tagline {
    position: absolute; left: 22px; top: 290px;
    color: var(--accent-green);
    font-weight: 500;
    line-height: 1;
  }
  .tagline .line-1 { font-size: 38px; display: block; }
  .tagline .line-2 { font-size: 38px; display: block; margin: 8px 0 0 50px; }
  .tagline .soft { font-weight: 300; font-size: 28px; }
  .rendering {
    position: absolute; left: 0; top: 392px; width: 380px; height: 320px;
  }
  .opening-banner {
    position: absolute; left: 70px; right: 0; top: 700px; height: 128px;
    background: linear-gradient(90deg, var(--gold-dark), var(--gold-light) 55%, #dcc392);
    border-left: 6px solid #5e4520;
    padding: 14px 0 0 22px;
    color: var(--sign-white);
    line-height: 1;
  }
  .opening-banner .label { font-size: 34px; font-weight: 300; color: #2a2014; letter-spacing: .5px; }
  .opening-banner .date { font-size: 64px; font-weight: 500; margin-top: 6px; }
  .website {
    position: absolute; left: 0; right: 0; top: 845px;
    text-align: center;
    font-size: 19px; color: var(--ink); font-weight: 400;
  }
</style>
</head>
<body>
  <main class="sign">
    <svg class="sign-top" width="380" height="880" viewBox="0 0 380 880" aria-hidden="true">
      <defs>
        <linearGradient id="bandShade" x1="0" y1="0" x2="0" y2="1">
          <stop offset="0" stop-color="#000"/>
          <stop offset="1" stop-color="#2b2b2b"/>
        </linearGradient>
      </defs>
      <path d="M0 0 H380 V262 Q190 252 0 272 Z" fill="url(#bandShade)"/>
      <path d="M0 272 Q190 252 380 262 V276 Q190 266 0 288 Z" fill="var(--accent-green)"/>
    </svg>

    <h1 class="brand-name">Harbor<br>Locker<br>Yard</h1>

    <p class="tagline">
      <span class="line-1"><span class="soft">Your</span> Premier</span>
      <span class="line-2">Self-Storage <span class="soft">facility</span></span>
    </p>

    <svg class="rendering" viewBox="0 0 380 320" role="img" aria-label="Architectural rendering of the new self-storage building with a tree in front">
      <defs>
        <linearGradient id="renderTones" x1="0" y1="0" x2="0" y2="1">
          <stop offset="0" stop-color="#e9e4d6"/>
          <stop offset=".55" stop-color="#cdb894"/>
          <stop offset=".8" stop-color="#a7a45a"/>
          <stop offset="1" stop-color="#6f8a2c"/>
        </linearGradient>
      </defs>
      <path d="M380 92 C320 40 250 10 180 12 C90 15 40 70 40 150 C40 230 100 290 170 308 L380 308 Z"
            fill="url(#renderTones)" stroke="var(--accent-green)" stroke-width="7"/>
    </svg>

    <div class="opening-banner">
      <div class="label">OPENING</div>
      <div class="date">FALL 2016</div>
    </div>

    <p class="website">www.harborlockeryard.example</p>
  </main>
</body>
</html>
```